Protein Powder Bag Design

We need a packaging design for a protein powder for our supplement company. The company is "Dawn Forward" and the product is called "SUMMIT PROTEIN"

The bag design needs to include:

- Our Logo
- Grass-Fed Beef Isolate Powder
- Chocolate (as the flavor)
- 2lbs 900grams Dietary Supplement
- Matte finish

The back of the bag needs to include:

- Blurb about Dawn Forward
i.e. Live Dawn Forward for anything and part of that means dialing in your nutrition. We are about clean, real, whole foods, quality, transparency, health, performance, flexible lifestyle, convenience, paleo friendly, no gluten

- Supplement Facts (attached)
*Under Supplement Facts*
INGREDIENTS: Grass-Fed Beef Protein (BovaPURE TM), Cocoa Powder, Stevia Leaf Powder

- Barcode (attached)
- #grabplainmeals
- info@dawnforwardfoods.example
- dawnforwardfoods.example
- Manufactured for Dawn Forward, San Francisco, Ca 94870
- Collagen/Gellatin
- Complete source of protein
- Free from: dairy, gluten, whey, soy, antibiotics, hormones, fillers, artificial sweeteners, preservatives, and other nonsense.

- Suggested Use:
Mix with 8 to 10 oz of liquid or add to baked foods to feel amazing. Store in a dry, cool place.

- Ingredients Per Scoop:
4 oz grass-fed beef
Cocoa Powder
Stevia

- **These statements have not been evaluated by The Bureau of Consumer Goods. This product is not intended to diagnose, treat, cure or prevent disease.

Requirements
Must have
• - Matte finish
• - Blue, white, color scheme
• - Check out the templates (do not copy)

```html
<!DOCTYPE html>
<html lang="en">
<head>
<meta charset="utf-8">
<title>Summit Protein – Chocolate Pouch Front</title>
<link rel="stylesheet" href="https://fonts.googleapis.com/css2?family=Barlow+Condensed:wght@500;600;700;800&family=Barlow:wght@500;600&display=swap">
<style>
  :root {
    --backdrop: #1eb4e8;
    --pouch-orange: #f2591c;
    --pouch-orange-deep: #e24c14;
    --brand-blue: #1e8fd6;
    --headline-white: #eeece8;
    --ink-white: #fbf4ee;
    --ribbon-red: #6e1b10;
    --cocoa-dark: #4a2a1c;
    --cocoa-mid: #7a4a33;
  }
  * { box-sizing: border-box; margin: 0; padding: 0; }
  html, body {
    width: 1200px; height: 1116px; overflow: hidden;
    background: var(--backdrop);
  }
  .canvas { position: relative; width: 1200px; height: 1116px; }
  .pouch {
    position: absolute; left: 320px; top: 78px; width: 560px; height: 960px;
    background: linear-gradient(100deg, var(--pouch-orange-deep) 0%, var(--pouch-orange) 30%, var(--pouch-orange) 75%, var(--pouch-orange-deep) 100%);
    overflow: hidden;
  }
  .brand-panel {
    position: absolute; left: 11px; top: 22px; width: 176px; height: 154px;
    background: var(--brand-blue);
    display: flex; align-items: flex-end; justify-content: center; padding-bottom: 22px;
  }
  .brand-name {
    font-family: "Barlow Condensed", sans-serif; font-weight: 600;
    font-size: 22px; letter-spacing: 5px; color: var(--ink-white);
    text-align: center; line-height: 1.15;
  }
  .headline {
    position: absolute; left: 62px; top: 270px;
    font-family: "Barlow Condensed", sans-serif; font-weight: 800;
    color: var(--headline-white); line-height: 0.86;
    text-transform: uppercase;
  }
  .headline .product-name { display: block; font-size: 96px; letter-spacing: 1px; }
  .headline .descriptor { display: block; font-weight: 700; }
  .descriptor.grass-fed { font-size: 46px; margin-top: 10px; }
  .descriptor.isolate { font-size: 62px; margin-top: 4px; }
  .descriptor.powder { font-size: 48px; margin-top: 2px; }
  .cocoa-visual {
    position: absolute; left: 341px; top: 430px; width: 219px; height: 132px;
    background: radial-gradient(ellipse at 45% 60%, var(--cocoa-mid) 0%, var(--cocoa-dark) 55%, rgba(74,42,28,0) 75%);
  }
  .flavor-ribbon {
    position: absolute; left: 165px; top: 620px; width: 264px; height: 44px;
    background: var(--ribbon-red);
    border: 2px solid rgba(255,255,255,0.55);
    display: flex; align-items: center; justify-content: center;
    font-family: "Barlow Condensed", sans-serif; font-weight: 600;
    font-size: 28px; letter-spacing: 3px; color: var(--ink-white);
  }
  .flavor-ribbon::before, .flavor-ribbon::after {
    content: ""; position: absolute; top: 8px; width: 22px; height: 28px; background: var(--ribbon-red); z-index: -1;
  }
  .flavor-ribbon::before { left: -16px; clip-path: polygon(0 0, 100% 0, 100% 100%, 0 100%, 35% 50%); }
  .flavor-ribbon::after { right: -16px; clip-path: polygon(0 0, 100% 0, 65% 50%, 100% 100%, 0 100%); }
  .per-scoop {
    position: absolute; left: 0; top: 690px; width: 100%; text-align: center;
    font-family: "Barlow", sans-serif; font-weight: 500; font-size: 17px; color: var(--ink-white);
  }
  .scoop-amount {
    position: absolute; left: 252px; top: 708px; display: flex; align-items: flex-start; gap: 6px;
    color: var(--ink-white);
  }
  .scoop-amount .number { font-family: "Barlow Condensed", sans-serif; font-weight: 600; font-size: 82px; line-height: 1; }
  .scoop-amount .unit { font-family: "Barlow Condensed", sans-serif; font-weight: 600; font-size: 28px; line-height: 1; margin-top: 20px; }
  .scoop-amount .unit small { display: block; font-family: "Barlow", sans-serif; font-weight: 500; font-size: 11px; line-height: 1.1; max-width: 60px; }
  .ingredient-strip {
    position: absolute; left: 99px; top: 803px; width: 429px; height: 48px;
    display: grid; grid-template-columns: 154px 128px 1fr;
    border: 1.5px solid var(--ink-white);
  }
  .ingredient-strip span {
    font-family: "Barlow Condensed", sans-serif; font-weight: 500; font-size: 20px;
    letter-spacing: 2px; color: var(--ink-white); line-height: 1;
    display: flex; align-items: center; justify-content: center;
  }
  .ingredient-strip span + span { border-left: 1.5px solid var(--ink-white); }
  .ingredient-strip .two-line { font-size: 17px; justify-content: flex-start; padding-left: 10px; }
  .supplement-label {
    position: absolute; left: 0; top: 880px; width: 100%; text-align: center;
    font-family: "Barlow", sans-serif; font-weight: 500; color: var(--ink-white); letter-spacing: 2px;
  }
  .supplement-label .type { display: block; font-size: 21px; }
  .supplement-label .weight { display: block; font-size: 17px; margin-top: 6px; letter-spacing: 1.5px; }
</style>
</head>
<body>
<main class="canvas">
  <section class="pouch">
    <div class="brand-panel">
      <span class="brand-name">DAWN<br>FORWARD</span>
    </div>
    <h1 class="headline">
      <span class="product-name">Summit</span>
      <span class="product-name">Protein</span>
      <span class="descriptor grass-fed">Grass-Fed Beef</span>
      <span class="descriptor isolate">Isolate</span>
      <span class="descriptor powder">Powder</span>
    </h1>
    <div class="cocoa-visual" role="img" aria-label="Photo of chocolate pieces on cocoa powder"></div>
    <div class="flavor-ribbon">CHOCOLATE</div>
    <p class="per-scoop">Per Scoop:</p>
    <div class="scoop-amount">
      <span class="number">4</span>
      <span class="unit">oz<small>grass-fed beef</small></span>
    </div>
    <div class="ingredient-strip">
      <span class="two-line">BEEF<br>ISOLATE</span>
      <span>COCOA</span>
      <span>STEVIA</span>
    </div>
    <p class="supplement-label">
      <span class="type">DIETARY SUPPLEMENT</span>
      <span class="weight">2lbs | 900grams</span>
    </p>
  </section>
</main>
</body>
</html>
```